High-end b2b furniture company needs informational/photo brochure

Please note CHANGE IN SIZE: 11 x 25.5 overall size, tri-fold brochure. Use lots of photos and must have a high-end, clean look because we are in the interior design industry. Designer must review our website to get an idea of branding! (www.halvorquist.example).

Instructions on where all photos/images should be placed are written as the file name for the jpgs/pdfs. Please ask if file name placement instructions are not clear!

There are extra images attached to use if needed, but you do not need to use all of these. There are also several images marked for the cover, but again, no need to use all of these if it looks too crowded. This will depend upon your design. (We would prefer a relatively clean, uncrowded look.)

Thank you for your hard work. I just increased the budget for first place on this project due to the large size of this brief.

Target Market(s)

Interior designers, architects, commercial property managers, shopping mall/retail managers. We sell commercial furniture ONLY (we do not sell to end consumers and we typically do not sell furniture for the home).

Industry/Entity Type

It Company

Font styles to use
Serif
Sans Serif
Other font styles liked:
• Prefer mostly sans serif, but can use serif if design calls for it. We use variations of Gil Sans MT in much of our marketing. Can use a decorative or script font for accent, but nothing that looks "old fashioned" and no cursive or anything that looks "curly."

Colors
cadf82
add136
faa54b
f78f20
ffffff

Requirements
Must have
• An upscale feel that appeals to high-end interior designers. Photography needs to be fairly large to highlight the furniture. (Text can be placed around furniture)
Nice to have
• Ample white and dark (black or charcoal gray) space
Should not have
• No old fashioned/cursive fonts. No shadows behind photos or shadows behind text boxes. Since furniture design is our business, do not cut off the lines of our furniture designs by overlapping text or images.

```html
<!DOCTYPE html>
<html lang="en">
<head>
<meta charset="utf-8">
<title>Halvorquist Furniture – Brochure Spread</title>
<link rel="stylesheet" href="https://fonts.googleapis.com/css2?family=Source+Sans+3:wght@400;600;700&display=swap">
<style>
  :root {
    --green-light: #cadf82;
    --green: #add136;
    --orange-light: #faa54b;
    --orange: #f78f20;
    --white: #ffffff;
    --backdrop: #e6e6e6;
    --ink: #2b2b2b;
    --ink-soft: #555555;
  }
  * { margin: 0; padding: 0; box-sizing: border-box; }
  html, body { width: 1200px; height: 900px; overflow: hidden; }
  body {
    background: var(--backdrop);
    font-family: "Source Sans 3", sans-serif;
    color: var(--ink);
    position: relative;
  }
  .spread {
    position: absolute;
    left: 80px; top: 80px;
    width: 1040px; height: 740px;
    display: flex;
    background: var(--white);
  }
  .page { position: relative; width: 520px; height: 740px; overflow: hidden; }

  /* Back page */
  .band { position: absolute; left: 0; width: 100%; }
  .band--top { top: 0; height: 100px; background: var(--green-light); }
  .band--quote-one { top: 100px; height: 200px; background: var(--orange-light); }
  .band--quote-two { top: 300px; height: 170px; background: var(--green-light); }
  .band--contact { top: 470px; height: 190px; background: var(--orange-light); }
  .band--footer { top: 660px; height: 80px; background: var(--white); }

  .wordmark {
    letter-spacing: 0.22em;
    text-transform: uppercase;
    font-weight: 400;
    line-height: 1.2;
  }
  .wordmark--back {
    position: absolute; right: 60px; top: 34px;
    color: var(--white);
    font-size: 20px;
    text-align: right;
  }

  .testimonial {
    position: absolute; left: 80px; width: 360px;
    font-size: 10px; line-height: 1.45;
    text-align: center;
    color: var(--ink);
  }
  .testimonial--one { top: 118px; }
  .testimonial--two { top: 330px; }
  .testimonial__author { display: block; margin-top: 4px; font-weight: 700; }
  .testimonial__role { display: block; font-weight: 700; }

  .contact-address {
    position: absolute; left: 40px; top: 600px;
    display: flex; gap: 8px; align-items: flex-start;
    font-size: 11px; line-height: 1.4;
    font-style: normal;
  }
  .contact-phones {
    position: absolute; right: 56px; top: 604px;
    font-size: 11px; line-height: 1.6;
  }
  .contact-phones li { list-style: none; display: flex; align-items: center; gap: 6px; }
  .footer-links {
    position: absolute; left: 40px; right: 40px; top: 690px;
    display: flex; justify-content: space-between;
    font-size: 11px; color: var(--ink);
  }

  /* Cover page */
  .cover-header {
    position: absolute; left: 0; top: 0; width: 100%; height: 150px;
    background: var(--white);
  }
  .wordmark--cover {
    position: absolute; right: 46px; top: 52px;
    color: var(--green);
    font-size: 30px;
    text-align: right;
  }
  .product-grid {
    position: absolute; left: 0; top: 150px;
    width: 520px; height: 510px;
    display: grid;
    grid-template-columns: 1fr 1fr;
    grid-template-rows: repeat(3, 1fr);
  }
  .product-grid__cell { display: flex; align-items: center; justify-content: center; }
  .product-grid__cell--green { background: var(--green-light); }
  .product-grid__cell--orange { background: var(--orange-light); }
  .product-photo { width: 170px; height: 126px; }
  .product-photo--wide { width: 200px; height: 110px; }
  .cover-footer {
    position: absolute; left: 0; top: 660px; width: 100%; height: 80px;
    display: flex; align-items: center; justify-content: center;
    font-size: 11px; letter-spacing: 0.45em; color: var(--ink-soft);
  }
</style>
</head>
<body>
  <main class="spread">
    <section class="page page--back">
      <div class="band band--top"></div>
      <div class="band band--quote-one"></div>
      <div class="band band--quote-two"></div>
      <div class="band band--contact"></div>
      <div class="band band--footer"></div>

      <p class="wordmark wordmark--back">Halvorquist Furniture</p>

      <blockquote class="testimonial testimonial--one">
        Your recent delivery completes a string of 3 successful hospitality installations. My client and I couldn't be more pleased with the workmanship and timely turn-around on product. Your suggestions for custom revisions to our favorite lounge chair (arm height, caster and seat cushion adjustments) have allowed us to use it throughout more areas of each hotel. That service, and continual new, fresh designs, keeps me coming back. I look forward to working with you on my next hotel and an upcoming medical project.
        <span class="testimonial__author">Mara Ellison</span>
        <span class="testimonial__role">Principal, Northline Studio</span>
      </blockquote>

      <blockquote class="testimonial testimonial--two">
        I have enjoyed using Halvorquist Furniture for myself &amp; my clients. I show the product every chance I get. I love that it's made in the USA, and I appreciate the design knowledge &amp; background that HQF brings to every order we place!
        <span class="testimonial__author">Renee Calder</span>
        <span class="testimonial__role">Principal, Open Plan Interiors</span>
      </blockquote>

      <address class="contact-address">
        <svg width="12" height="18" viewBox="0 0 12 18" aria-hidden="true">
          <path d="M6 0C2.7 0 0 2.6 0 5.9 0 10 6 18 6 18s6-8 6-12.1C12 2.6 9.3 0 6 0z" fill="#555"/>
          <circle cx="6" cy="6" r="2.3" fill="#faa54b"/>
        </svg>
        <span>48 Orchard Lane, Suite 310<br>Cedar Falls, OR 97000</span>
      </address>

      <ul class="contact-phones">
        <li>
          <svg width="10" height="10" viewBox="0 0 10 10" aria-hidden="true">
            <path d="M2 0.5 L3.6 2.6 L2.7 3.6 C3.3 5 4.8 6.6 6.3 7.3 L7.4 6.4 L9.5 8 L8.4 9.5 C4.5 9 1 5.5 0.5 1.6 Z" fill="#555"/>
          </svg>
          888 555 0140
        </li>
        <li>
          <svg width="10" height="10" viewBox="0 0 10 10" aria-hidden="true">
            <rect x="0.5" y="3" width="9" height="6" rx="1" fill="#555"/>
            <rect x="2.5" y="0.5" width="5" height="3" fill="#555"/>
          </svg>
          888 555 0187
        </li>
      </ul>

      <div class="footer-links">
        <span>www.halvorquist.example</span>
        <span>customerservice@halvorquist.example</span>
      </div>
    </section>

    <section class="page page--cover">
      <header class="cover-header">
        <p class="wordmark wordmark--cover">Halvorquist<br>Furniture</p>
      </header>

      <div class="product-grid">
        <div class="product-grid__cell product-grid__cell--green">
          <svg class="product-photo" role="img" aria-label="Photo of an orange upholstered wingback lounge chair"><rect width="100%" height="100%" fill="#e8782a"/></svg>
        </div>
        <div class="product-grid__cell product-grid__cell--orange">
          <svg class="product-photo" role="img" aria-label="Photo of a tan leather armchair on dark legs"><rect width="100%" height="100%" fill="#b9a877"/></svg>
        </div>
        <div class="product-grid__cell product-grid__cell--orange">
          <svg class="product-photo" role="img" aria-label="Photo of a teal velvet tufted club chair"><rect width="100%" height="100%" fill="#2f5360"/></svg>
        </div>
        <div class="product-grid__cell product-grid__cell--green">
          <svg class="product-photo" role="img" aria-label="Photo of a grey modern lounge chair with wooden legs"><rect width="100%" height="100%" fill="#6d6765"/></svg>
        </div>
        <div class="product-grid__cell product-grid__cell--green">
          <svg class="product-photo product-photo--wide" role="img" aria-label="Photo of a beige upholstered settee"><rect width="100%" height="100%" fill="#c9bd9e"/></svg>
        </div>
        <div class="product-grid__cell product-grid__cell--orange">
          <svg class="product-photo product-photo--wide" role="img" aria-label="Photo of a light grey button-tufted sofa"><rect width="100%" height="100%" fill="#cfcdca"/></svg>
        </div>
      </div>

      <footer class="cover-footer">www.halvorquist.example</footer>
    </section>
  </main>
</body>
</html>
```